Herb Farm - Tea Label Design

We are a small herbalist company called 'Meadowlark Tisanes' which requires a new label scheme.

Meadowlark Tisanes specializes in organic wellness teas, handmade soaps, bath and beauty products. We also offer local beeswax, pollen and an herb CSA.

Our slogan is "Ancient Remedies for Modern Life" and we frequently market ourselves as an "Apothecary & Herb Farm".

The primary use of this label will be on tins and biodegradable food grade paper bags.

We are looking for:

1) An unique universal design for our products. Something that we can put on the tea tins/bags as well as boxes in the future. To keep costs down I would like something that can be used on a variety of products by simply having the colour changed or adding the title of the product in a certain area. We have four collections. Please see the attached style guide. I particularly like the Silver Kettle Brew Co. as each type of tea is reprinted by a design. Please see their website for further clarification. I also really like their styling.

2) Label required is 8.5" x 5.25" (w - h). Bear in mind we also have dark cobalt blue jars and Brunel biodegradable bags available that this label will fit on (5570-02 as pictured)

3) We would like to see a design that is colourful, and has elements of modern simplicity yet certainly has an old world apothecary charm.

4) Please refer to our current label for product information. Not everything has to be in the same place in the new design, however all the information is required.

We will require source files in .ai and .eps (layers retained, no outlines on text, list of fonts used).

Please visit: www.meadowlarktisanes.example

We included a few favourites and the styles we prefer, but please be creative!

The label chosen could be in for a lot more design work as we expand our company. Any other input regarding packaging would be helpful.
Updates

Hello Designers!

I have posted our current label for you to review - I like it, yet I don't. You can see the level of craftsman ship brings up to artisan, and mid-high range product. The only parts I really want to keep from this label is how the brewing instructions are set out.

In terms of design, I do not want to use a photograph on the label - it is there for inspiration!

Thanks,
Meadowlark Tisanes 

Reason: I would like to see more designs, from a variety of designers for this label project.

Reason: Would like to see more designs.

Reason: In receiving designs I realized that the sizing is not ideal as it does not have ample space for the required information. I have updated the brief to reflect this and posted a working file that has the required elements. A lot of good designs, but I noticed the over use of filigree or Victorian ornamentation. I would like some ornamentation but simplicity is desired in the overall label. There was not enough designs submitted, nothing that truly wow-ed me. I hope to see more unique designs! Thanks.

Target Market(s)

30-something, retired, eco-conscious, women, mid-priced marketing, local Ontario Canada; some products will be sold at a local historical village

Industry/Entity Type

Biodegradable

Font styles to use
Decorative
Other font styles liked:
• DellaRobbia BT Bold; Foglihten No07

Requirements
Must have
• Fonts used: Dellarobbia BT Bold and Foglihten No07
Use fonts and logo design; you can use separate leaf components but fonts chosen for logo cannot change

Other fonts can be used but please use Foglihten No07 for "Meadowlark Tisanes" and Dellarobbia BT Bold for "Apothecary & Herb Farm" and for "Ancient Remedies for Modern Life".
Nice to have
• "Apothecary & Herb Farm" or slogan
Should not have
• Comic sans
clipart
Filigree or line swooshes

```html
<!DOCTYPE html>
<html lang="en">
<head>
<meta charset="utf-8">
<title>Meadowlark Tisanes – Hedgerow White Tea Label</title>
<link rel="stylesheet" href="https://fonts.googleapis.com/css2?family=Arimo:wght@400;700&family=Tinos:ital@1&display=swap">
<style>
  :root {
    --page: #ffffff;
    --leaf-green: #8dbb22;
    --lime: #c9dd3c;
    --sun: #f2ef9a;
    --ink: #4a4a38;
    --ink-soft: #5a5a45;
    --band-light: #b6d53a;
    --band-dark: #7e8a02;
    --band-dark-text: #cdd27a;
  }
  * { box-sizing: border-box; margin: 0; padding: 0; }
  html, body { width: 1200px; height: 1000px; overflow: hidden; background: var(--page); }
  body { position: relative; font-family: "Arimo", Arial, sans-serif; color: var(--ink); }

  .label {
    position: absolute; left: 123px; top: 210px; width: 954px; height: 586px;
    border: 1px solid #6b7a2a;
    background: linear-gradient(90deg, var(--leaf-green) 0%, var(--lime) 22%, var(--sun) 42%, #f6f2a4 50%, var(--sun) 58%, var(--lime) 78%, var(--leaf-green) 100%);
    overflow: hidden;
  }
  .center-art {
    position: absolute; left: 207px; top: 0; width: 540px; height: 586px;
    background:
      radial-gradient(ellipse at 50% 72%, rgba(233,225,90,.8), rgba(233,225,90,0) 55%),
      radial-gradient(ellipse at 18% 35%, rgba(167,207,82,.5), rgba(167,207,82,0) 40%),
      radial-gradient(ellipse at 82% 35%, rgba(167,207,82,.5), rgba(167,207,82,0) 40%);
  }

  .panel { position: absolute; text-align: center; color: var(--ink-soft); }
  .panel p { margin-bottom: 13px; }
  .panel-left { left: 17px; width: 200px; top: 30px; font-size: 11.5px; line-height: 13px; }
  .panel-right { left: 732px; width: 182px; top: 38px; font-size: 10.5px; line-height: 13.5px; }

  .nutrition { position: absolute; left: 56px; top: 336px; width: 150px; font-size: 9px; line-height: 9.6px; color: var(--ink-soft); text-align: left; }
  .nutrition h3 { font-weight: 400; font-size: 15px; line-height: 15px; color: var(--ink); }
  .nutrition .row { display: flex; }
  .nutrition .row span:first-child { flex: 0 0 100px; }
  .nutrition .note { margin-top: 1px; font-size: 8px; line-height: 8.6px; }

  .brand { position: absolute; left: 227px; width: 500px; text-align: center; font-weight: 400; }
  .brand-name { top: 36px; font-size: 40px; line-height: 48px; color: var(--ink); }
  .brand-name .line2 { display: block; font-size: 56px; line-height: 58px; }
  .brand-sub { top: 164px; font-size: 11px; letter-spacing: 7px; line-height: 13px; color: var(--ink); text-transform: uppercase; }
  .slogan { top: 200px; font-size: 15px; color: var(--ink); }

  .rule { position: absolute; }
  .product-name { position: absolute; left: 335px; width: 300px; top: 324px; text-align: center; font-size: 32px; font-weight: 400; color: var(--ink); }
  .band { position: absolute; left: 333px; width: 305px; text-align: center; }
  .band-type { top: 372px; height: 25px; background: var(--band-light); font-size: 17px; line-height: 25px; color: var(--ink); }
  .band-kind { top: 398px; height: 18px; background: var(--band-dark); font-size: 12px; line-height: 18px; color: var(--band-dark-text); }
  .net-wt { position: absolute; left: 335px; width: 300px; top: 492px; text-align: center; font-size: 14px; color: var(--ink); }

  .latin { font-family: "Tinos", serif; font-style: italic; font-size: 8px; }
  .brew { display: grid; grid-template-columns: 1fr 1fr; row-gap: 8px; margin: 30px -8px 22px; font-size: 13px; color: var(--ink); text-align: left; }
  .brew div { display: flex; align-items: center; gap: 6px; white-space: nowrap; }
  .brew svg { flex: none; }
</style>
</head>
<body>
<main class="label">
  <div class="center-art" role="img" aria-label="Soft mirrored watercolour botanical illustration of yellow and green leaves and a teacup"></div>

  <section class="panel panel-left">
    <p>Always consult a medical practioner before trying any new herbs. Plants are medicine and should be treated as such. Discontinue use immediately if you develop discomfort and consult a doctor familiar with herbal treatments.</p>
    <p>Expires:</p>
    <p>Blended and packaged by<br>Fern Hill Tea, Perth ON CANADA<br>for Meadowlark Tisanes<br>Alder Falls ON N0B 2X4 CANADA</p>
    <p>For product and nutritional information visit us online at:<br>www.meadowlarktisanes.example<br>info@meadowlarktisanes.example</p>
  </section>

  <section class="nutrition">
    <h3>Nutrition Facts</h3>
    <div>Serving Size: 1 teaspoon (2.5 g)</div>
    <div>Serving Per Container: 40</div>
    <div>Amount Per Serving</div>
    <div class="row"><span>Calories: 0</span><span>Cal from</span></div>
    <div>Fat: 0</div>
    <div class="row" style="margin-top:4px"><span></span><span>% Daily<br>&nbsp;&nbsp;Value*</span></div>
    <div class="row"><span>Total Fat Less than 0g</span><span>0%</span></div>
    <div class="row"><span>Saturated Fat 0g</span><span>0%</span></div>
    <div class="row"><span>Trans Fat 0g</span><span>0%</span></div>
    <div class="row"><span>Polyunsaturated Fat 0g</span><span>0%</span></div>
    <div class="row"><span>Monounsaturated Fat 0g</span><span>0%</span></div>
    <div class="row"><span>Cholesterol 0mg</span><span>0%</span></div>
    <div class="row"><span>Sodium 0mg</span><span>0%</span></div>
    <div class="row"><span>Total Carb 0g</span><span>0%</span></div>
    <div class="row"><span>Protein 0g</span><span>0%</span></div>
    <div class="note">Not a significant source of dietary fiber, sugar, vitamin A and C, calcium and iron. *Percent Daily Values are based on a 2000 calorie diet.</div>
  </section>

  <h1 class="brand brand-name">Meadowlark<span class="line2">Tisanes</span></h1>
  <div class="brand brand-sub">Apothecary<br>&amp; Herb Farm</div>
  <div class="brand slogan">Old Wisdom for Everyday Living</div>

  <svg class="rule" style="left:330px;top:300px" width="310" height="12" viewBox="0 0 310 12">
    <line x1="5" y1="6" x2="305" y2="6" stroke="#4a4a38" stroke-width="1.5"/>
    <circle cx="5" cy="6" r="2.5" fill="#4a4a38"/><circle cx="305" cy="6" r="2.5" fill="#4a4a38"/>
  </svg>

  <h2 class="product-name">Hedgerow</h2>
  <div class="band band-type">White Tea</div>
  <div class="band band-kind">Floral infusion</div>

  <svg class="rule" style="left:360px;top:494px" width="20" height="14" viewBox="0 0 20 14">
    <path d="M2 7 H16 M10 2 L16 7 L10 12" stroke="#4a4a38" stroke-width="1.6" fill="none"/>
  </svg>
  <div class="net-wt">NET WT.&nbsp; 35 g / 1.2 oz</div>
  <svg class="rule" style="left:592px;top:494px" width="20" height="14" viewBox="0 0 20 14">
    <path d="M18 7 H4 M10 2 L4 7 L10 12" stroke="#4a4a38" stroke-width="1.6" fill="none"/>
  </svg>

  <svg class="rule" style="left:358px;top:528px" width="254" height="16" viewBox="0 0 254 16">
    <path d="M4 6 H118 Q124 6 124 12 M250 6 H136 Q130 6 130 12" stroke="#4a4a38" stroke-width="1.5" fill="none"/>
    <circle cx="4" cy="6" r="2.5" fill="#4a4a38"/><circle cx="250" cy="6" r="2.5" fill="#4a4a38"/>
  </svg>

  <section class="panel panel-right">
    <p>Discover a gentle meeting of meadow and highland botanicals in our soft white tea, wild rose and heather blend. This bright and fragrant pairing is as delightful as it is restorative.</p>
    <p style="margin-top:24px">Ingredients: Organic white tea <span class="latin">(Camellia sinensis)</span>, organic rose petals (<span class="latin">Rosa rubiginosa</span>) and organic scotch heather (<span class="latin">Calluna vulgaris</span>).</p>
    <p>For a cup brewed just right please follow these steps:</p>
    <div class="brew">
      <div><svg width="18" height="18" viewBox="0 0 18 18"><circle cx="9" cy="9" r="7.5" fill="none" stroke="#4a4a38" stroke-width="1.3"/><path d="M9 4 V9 H12" stroke="#4a4a38" stroke-width="1.2" fill="none"/></svg>2 - 3 min</div>
      <div><svg width="18" height="18" viewBox="0 0 18 18"><circle cx="9" cy="9" r="8.5" fill="#4a4a38"/></svg>2.5 g / 1 tsp</div>
      <div style="padding-left:4px">177 mL / 6 oz</div>
      <div><svg width="14" height="18" viewBox="0 0 14 18"><path d="M7 1 C9 6 13 9 13 12 A6 6 0 0 1 1 12 C1 9 5 6 7 1Z" fill="#4a4a38"/></svg>80C / 176F</div>
    </div>
    <p>MEADOWLARK TISANES<br>APOTHECARY &amp; HERB FARM</p>
    <p>Every oil we use is purely plant-based, our teas come from organic and responsible growers, and we gather wild herbs with great care.</p>
    <p>Our products never contain harsh detergents, artificial colours, synthetic scents, preservatives, palm oil or fillers of any kind.</p>
    <p>Only wholesome, nourishing herbs<br>and calming ingredients.</p>
    <p>Simple care for the land<br>and everything it grows.</p>
  </section>
</main>
</body>
</html>
```